7 page website for Dog Training Business

we are seeking a website design that should be 7 pages for a Las Vegas Dog training business. the site will have a heavy focus on video, and social media. Ideas design can be borrowed from http://plumcrestway.net
attached is a copy of the logo and business card mock up. Content is currently being written and will be posted shortly

Training

```html
<!DOCTYPE html>
<html lang="en">
<head>
<meta charset="utf-8">
<title>Pawstead Dog Training</title>
<link href="https://fonts.googleapis.com/css2?family=Oswald:wght@300;400;500&family=Roboto:ital,wght@0,400;1,400&display=swap" rel="stylesheet">
<style>
:root{
  --lime:#bcd65e;
  --lime-dark:#a9c64a;
  --brown:#7a4222;
  --brown-text:#6d3a1c;
  --green:#3e5d42;
  --ink:#555;
  --white:#fff;
}
*{margin:0;padding:0;box-sizing:border-box}
html,body{width:812px;height:1200px;overflow:hidden}
body{position:relative;background:linear-gradient(180deg,#c6de6e 0,#e6f1c0 220px,#fff 380px);font-family:'Roboto',sans-serif;color:var(--ink)}
.page{position:absolute;left:40px;top:0;width:730px;height:1098px;background:var(--white)}
.abs{position:absolute}
.nav{position:absolute;left:50px;top:35px;width:712px;height:32px}
.nav a{position:absolute;top:11px;font-family:'Oswald',sans-serif;font-size:11px;color:#3a3a2a;text-decoration:none;letter-spacing:.2px}
.nav a.active{color:var(--brown)}
.logo{position:absolute;left:369px;top:14px;width:74px;height:74px;border-radius:50%;background:var(--lime);border:3px solid var(--brown);box-shadow:0 0 0 3px #fff inset;display:flex;align-items:center;justify-content:center;font-family:'Oswald',sans-serif;font-weight:500;font-size:13px;color:var(--brown)}
.hero{position:absolute;left:50px;top:76px;width:712px;height:270px;border:2px solid #d8d8d8;background:linear-gradient(100deg,#8fb33c 0,#b9d470 40%,#a7c45a 70%,#6e9430 100%)}
.hero-cap{position:absolute;left:3px;background:rgba(110,62,28,.88);color:#fff;font-family:'Oswald',sans-serif;font-weight:300;font-size:30px;line-height:40px;padding:0 16px}
.dots{position:absolute;left:20px;top:248px;display:flex;gap:3px}
.dots i{width:8px;height:8px;border-radius:50%;background:#333}
h2.sec{font-family:'Oswald',sans-serif;font-weight:400;color:var(--brown-text);font-size:18px}
.welcome p{font-size:8.5px;line-height:14.4px;width:458px;margin-top:6px}
.badge{position:absolute;top:401px;width:70px;height:70px;border-radius:50%}
.trainer{position:absolute;left:50px;top:482px;width:712px;height:150px;background:linear-gradient(90deg,#7c4a24 0,#8a4e25 60%,#75411f 100%);border:1px solid #6a391a}
.trainer .photo{position:absolute;left:0;top:0;width:246px;height:148px;background:linear-gradient(90deg,#a9c55a,#6f8a3a 60%,#8a4e25)}
.trainer .frame{position:absolute;inset:4px;border:1px solid rgba(255,255,255,.45)}
.trainer .kicker{position:absolute;left:254px;top:48px;font-family:'Oswald',sans-serif;font-size:16px;color:var(--lime)}
.trainer .name{position:absolute;left:253px;top:62px;font-family:'Oswald',sans-serif;font-size:36px;color:#fff;letter-spacing:-.3px}
.tile{position:absolute;top:645px;width:164px;height:135px;background:var(--lime)}
.tile .img{height:102px;background:linear-gradient(160deg,#8ea458,#6c6a44)}
.tile span{display:block;padding:4px 11px;font-family:'Oswald',sans-serif;font-size:16px;color:#3e4a22}
.dvd{position:absolute;left:50px;top:796px;width:529px;height:144px;background:radial-gradient(circle at 75% 40%,#4e7553,var(--green) 65%)}
.dvd h3{position:absolute;left:18px;top:13px;font-family:'Oswald',sans-serif;font-weight:400;font-size:17px;color:var(--lime)}
.dvd p{position:absolute;left:18px;top:42px;width:320px;font-size:8px;line-height:14.4px;color:#e8efe4}
.btn{position:absolute;left:20px;top:110px;width:128px;height:24px;background:var(--lime);font-family:'Oswald',sans-serif;font-size:12px;color:#3a3a1c;text-align:center;line-height:24px}
.discs{position:absolute;left:350px;top:14px;width:140px;height:118px;background:linear-gradient(135deg,#c9d3d0,#7f9a90);border-radius:6px}
.connect{position:absolute;left:598px;top:796px;width:164px;height:144px;background:var(--brown)}
.connect h3{position:absolute;left:16px;top:10px;font-family:'Oswald',sans-serif;font-weight:400;font-size:17px;color:var(--lime)}
.connect ul{list style:none;list-style:none;position:absolute;left:18px;top:38px}
.connect li{display:flex;align-items:center;height:23px;font-size:9px;color:#fff}
.connect li svg{margin-right:10px}
.testi h2{text-align:center}
.quote{position:absolute;top:1004px;width:224px;font-size:8px;line-height:14.4px;font-style:italic;color:#666}
.quote b{font-family:'Oswald',sans-serif;font-style:normal;font-size:14px;color:var(--brown);margin-right:3px;line-height:0}
.quote .who{display:block;margin-top:6px;color:var(--brown);font-size:8px}
.footer{position:absolute;left:0;top:1098px;width:812px;height:102px;background:var(--green)}
.footer nav a{position:absolute;top:25px;font-family:'Oswald',sans-serif;font-size:10px;color:#fff;text-decoration:none}
.footer .copy{position:absolute;left:50px;top:55px;font-size:8px;line-height:13px;color:#dfe8dc}
.contact{position:absolute;left:636px;font-family:'Oswald',sans-serif;font-size:14px;color:var(--lime);display:flex;align-items:center;gap:8px}
</style>
</head>
<body>
<div class="page"></div>

<header class="nav">
  <svg class="abs" width="712" height="32" viewBox="0 0 712 32"><polygon points="0,0 712,0 700,16 712,32 0,32 12,16" fill="#bcd65e"/><rect x="0" y="30" width="712" height="2" fill="#a9c64a"/></svg>
  <a class="active" style="left:26px">HOME</a>
  <a style="left:87px">ABOUT US</a>
  <a style="left:168px">SERVICES</a>
  <a style="left:245px">GALLERY</a>
  <a style="left:428px">TESTIMONIALS</a>
  <a style="left:525px">BLOG</a>
  <a style="left:584px">FAQ</a>
  <a style="left:636px">CONTACT US</a>
</header>
<div class="logo">PAWSTEAD</div>

<section class="hero" role="img" aria-label="Smiling trainer hugging a husky on a sunny lawn">
  <div class="hero-cap" style="top:92px">We are a Dog Training</div>
  <div class="hero-cap" style="top:134px">Business in US</div>
  <div class="dots"><i></i><i></i><i></i><i></i></div>
</section>

<section class="welcome abs" style="left:50px;top:368px">
  <h2 class="sec">Welcome to Our Website</h2>
  <p>Lorem ipsum dolor sit amet, consect- etuer adipiscing elit, sed diam nonummy nibh euismod tincidunt ut laoreet dolore magna aliquam erat volutpat. Ut wisi enim ad minim veniam, quis nostrud exerci tation ullam. Consectetuer adipiscing elit, sed diam nonummy nibh euismod tincidunt ut laoreet dolore magna aliquam erat volut- pat. Ut wisi enim ad minim veniam, quis nostrud exerci tation ullam. Aenean a nibh eget turpis vehicula tempus ac sed massa. Vestibulum dolor nulla, ultrices ac tincidunt sed, laoreet non est.</p>
</section>
<h2 class="sec abs" style="left:555px;top:369px;font-size:15px">NCTA PROFESSIONAL MEMBER #4812</h2>
<div class="badge" style="left:535px;background:#f3eee6;border:3px solid #d9b98d"></div>
<div class="badge" style="left:611px;background:#2f4c8f;border:3px solid #d0d7e6"></div>
<div class="badge" style="left:690px;background:#e3c72c;border:3px solid #2a4f8a"></div>

<section class="trainer">
  <div class="photo" role="img" aria-label="Trainer smiling beside a white bulldog outdoors"></div>
  <div class="frame"></div>
  <div class="kicker">MEET FAMILY DOG TRAINER</div>
  <div class="name">MARCUS DOG TRAINER</div>
  <svg class="abs" style="left:578px;top:32px" width="86" height="86" viewBox="0 0 86 86"><circle cx="43" cy="43" r="40" fill="none" stroke="#fff" stroke-width="4"/><polygon points="32,22 64,43 32,64 40,43" fill="#fff"/></svg>
</section>

<a class="tile" style="left:50px"><div class="img" role="img" aria-label="Trainer hugging a white dog"></div><span>Services/Rates</span></a>
<a class="tile" style="left:232px"><div class="img" role="img" aria-label="Person greeting a black and white dog"></div><span>Gallery</span></a>
<a class="tile" style="left:415px"><div class="img" role="img" aria-label="Man sitting with a labrador and a rottweiler"></div><span>Testimonials</span></a>
<a class="tile" style="left:598px"><div class="img" role="img" aria-label="Boxer dogs on leash"></div><span>FAQ</span></a>

<section class="dvd">
  <h3>The Good Dog Training DVD Series</h3>
  <p>Lorem ipsum dolor sit amet, consect- etuer adipiscing elit, sed diam nonummy nibh euismod tincidunt ut laoreet dolore magna aliquam erat volutpat. Ut wisi enim ad minim veniam, quis nostrud exerci tation ullam. Consectetuer adipiscing elit, sed diam nonummy nibh euismod tincidunt ut laoreet dolore magna aliquam erat..</p>
  <div class="btn">PURCHSE /READ MORE</div>
  <div class="discs" role="img" aria-label="Stack of DVD cases with discs"></div>
</section>

<aside class="connect">
  <h3>Connect Us</h3>
  <ul>
    <li><svg width="20" height="20"><circle cx="10" cy="10" r="9" fill="#3b5a9a" stroke="#fff" stroke-width="1.5"/></svg>Community</li>
    <li><svg width="20" height="20"><circle cx="10" cy="10" r="9" fill="#2aa3dc" stroke="#fff" stroke-width="1.5"/></svg>News Feed</li>
    <li><svg width="20" height="20"><circle cx="10" cy="10" r="9" fill="#c4302b" stroke="#fff" stroke-width="1.5"/></svg>Video Channel</li>
    <li><svg width="20" height="20"><circle cx="10" cy="10" r="9" fill="#6b7fa8" stroke="#fff" stroke-width="1.5"/><rect x="5.5" y="7" width="9" height="6" fill="#fff"/><polyline points="5.5,7 10,10.5 14.5,7" fill="none" stroke="#6b7fa8" stroke-width="1"/></svg>Email Us</li>
  </ul>
</aside>

<section class="testi">
  <h2 class="sec abs" style="left:0;width:812px;top:960px;text-align:center">Testimonials</h2>
  <div class="quote" style="left:50px"><b>“</b>Lorem ipsum dolor sit amet, consect- etuer adipiscing elit, sed diam nonummy nibh euismod tincidunt ut laoreet dolore magna aliquam erat volutpat. Ut wisi enim ad minim veniam, quis nostrud exerci tation ullam.....<span class="who">-Name Goes Here</span></div>
  <div class="quote" style="left:295px"><b>“</b>Lorem ipsum dolor sit amet, consect- etuer adipiscing elit, sed diam nonummy nibh euismod tincidunt ut laoreet dolore magna aliquam erat volutpat. Ut wisi enim ad minim veniam, quis nostrud exerci tation ullam.....<span class="who">-Name Goes Here</span></div>
  <div class="quote" style="left:538px"><b>“</b>Lorem ipsum dolor sit amet, consect- etuer adipiscing elit, sed diam nonummy nibh euismod tincidunt ut laoreet dolore magna aliquam erat volutpat. Ut wisi enim ad minim veniam, quis nostrud exerci tation ullam.....<span class="who">-Name Goes Here</span></div>
</section>

<footer class="footer">
  <nav>
    <a style="left:50px">HOME</a><a style="left:90px">ABOUT US</a><a style="left:147px">SERVICES</a><a style="left:200px">GALLERY</a><a style="left:251px">TESTIMONIALS</a><a style="left:336px">BLOG</a><a style="left:388px">FAQ</a><a style="left:433px">CONTACT US</a>
  </nav>
  <div class="copy">Copyright © 2015. Company Name. All Right Reserved<br>Term of Services</div>
  <div class="contact" style="top:23px;left:638px"><svg width="13" height="11" viewBox="0 0 13 11"><path d="M1 4 Q6.5 -1 12 4 L10 5 L9 3 L4 3 L3 5 Z" fill="#bcd65e"/><rect x="2" y="6" width="9" height="5" rx="1" fill="#bcd65e"/></svg>555-014-2290</div>
  <div class="contact" style="top:46px;left:638px"><svg width="13" height="10" viewBox="0 0 13 10"><rect width="13" height="10" fill="#bcd65e"/><polyline points="0,0 6.5,5 13,0" fill="none" stroke="#3e5d42" stroke-width="1.2"/></svg>hello@pawsteadk9.com</div>
</footer>
</body>
</html>
```